依頼詳細
ロゴはミナモワークスで作成していただいていますので、それを使用していただいきたいです。ホームページは現在作成中です。ロゴを取り入れ、柔らかい雰囲気でシンプルなイメージ、わかりやすい感じがいいです。
記載項目
病院名、ロゴ、開業日、内覧会の日程、住所、電話番号、ホームページのアドレス、診察時間、休診日 対象動物、挨拶等
サイズ
A4
ページ数
片面
希望イメージ
シンプル 複雑
単色 カラフル
暗い 明るい
日常 高級
遊び心 厳粛
未来的 伝統的
女性的 男性的
希望する色
納品ファイル
補足説明
ロゴを添付します。

挨拶内容
「はじめまして、はるかぜペットクリニック院長の森岡健司です。大学卒業後、熊本市内の動物病院で7年間勤務し、2014年3月24日に動物病院を開院することになりました。
ホームドクターとして地域の皆様に親しまれる病院であるとともに、飼い主様と一緒に家族である動物たちの最善のケアができるように努めてまいりたいと思います。ワンちゃん達が遊べるスペースも少しですが用意してあります。ぜひ気軽に遊びにいらしてください。今後ともよろしくお願い致します。」
おそくなりましたが、ホームページのドメイン決まりました。
http://harukaze-petclinic.exampleです。
よろしくお願いいたします。
■ 選んだ理由

シンプルで開院ということがわかりやすかったため。
犬の写真の雰囲気も良かったです。

■ 提案者全員のお礼・コメント

いいデザインを多数いただいてありがとうございます。それぞれおもしろくけっこう悩ませていただきました。また、よろしくお願いいたします。

```html
<!DOCTYPE html>
<html lang="ja">
<head>
<meta charset="utf-8">
<title>はるかぜペットクリニック 開院のお知らせ</title>
<link rel="stylesheet" href="https://fonts.googleapis.com/css2?family=M+PLUS+Rounded+1c:wght@400;700;800&display=swap">
<style>
  :root {
    --green: #8dbb2e;
    --green-dark: #6f9a1c;
    --brown: #5a3d2b;
    --cream: #f5f0e2;
    --cream-dark: #e9dfc8;
    --white: #ffffff;
    --text: #4a3a2e;
  }
  html, body { margin: 0; padding: 0; overflow: hidden; }
  body { width: 849px; height: 1200px; background: var(--cream); }
  .flyer {
    position: relative; width: 849px; height: 1200px; overflow: hidden;
    background: var(--cream);
    font-family: "M PLUS Rounded 1c", sans-serif; color: var(--text);
  }
  .abs { position: absolute; }
  .tagline { left: 0; right: 0; top: 22px; text-align: center; font-size: 26px; font-weight: 700; color: var(--brown); }
  .clinic-title { left: 0; right: 0; top: 60px; text-align: center; font-size: 64px; font-weight: 800; color: var(--brown); letter-spacing: 2px; }
  .clinic-title .accent { color: var(--green); }
  .open-date { left: 70px; top: 148px; font-size: 66px; font-weight: 800; color: var(--green); }
  .open-date small { font-size: 44px; }
  .open-word { left: 60px; top: 232px; display: flex; align-items: center; font-size: 128px; font-weight: 800; color: var(--green); line-height: 1; }
  .open-ring {
    width: 118px; height: 118px; border-radius: 50%; border: 14px solid var(--green);
    box-sizing: border-box; display: flex; align-items: center; justify-content: center;
    font-size: 30px; font-weight: 800; color: var(--green); margin-right: 4px;
  }
  .puppy-photo {
    left: 430px; top: 250px; width: 419px; height: 600px;
    background: radial-gradient(ellipse at 55% 45%, #f2dcb6 0%, #e7cda3 40%, #efe6d4 75%, var(--cream) 100%);
  }
  .preview-badge {
    left: 600px; top: 150px; width: 215px; height: 190px; border-radius: 50%;
    background: var(--white); border: 4px solid var(--green); box-sizing: border-box;
    text-align: center; color: var(--green); font-weight: 800;
    display: flex; flex-direction: column; justify-content: center;
  }
  .preview-badge .lead { font-size: 17px; }
  .preview-badge .event { font-size: 36px; line-height: 1.15; }
  .preview-badge .dates { font-size: 22px; }
  .preview-badge .invite { font-size: 13px; color: var(--brown); margin-top: 4px; }
  .greeting {
    left: 57px; top: 375px; width: 480px; height: 235px; box-sizing: border-box;
    background: var(--white); border: 3px solid var(--cream-dark); border-radius: 10px; padding: 18px 22px;
  }
  .greeting-head { display: flex; align-items: center; gap: 12px; margin-bottom: 10px; }
  .greeting-icon { width: 56px; height: 56px; border-radius: 50%; background: #e9e4d8; }
  .greeting-head h2 { margin: 0; font-size: 24px; color: var(--brown); font-weight: 800; }
  .greeting p { margin: 0; font-size: 12.5px; line-height: 1.65; }
  .animals { left: 57px; top: 630px; display: flex; align-items: center; gap: 14px; font-size: 20px; font-weight: 700; color: var(--brown); }
  .label { background: var(--green); color: var(--white); font-size: 16px; font-weight: 700; padding: 4px 12px; }
  .hours { left: 57px; top: 675px; width: 480px; border-collapse: collapse; font-size: 15px; text-align: center; }
  .hours th, .hours td { border-bottom: 2px solid var(--cream-dark); padding: 7px 0; background: var(--white); }
  .hours th { font-weight: 700; color: var(--brown); }
  .hours th.label-cell { background: var(--green); color: var(--white); width: 100px; }
  .hours td.time { font-weight: 700; color: var(--brown); }
  .hours .dot { color: var(--green); font-size: 18px; }
  .hours .closed { font-size: 13px; color: var(--brown); }
  .note { left: 57px; top: 795px; font-size: 11px; }
  .map {
    left: 545px; top: 630px; width: 260px; height: 260px; border-radius: 50%;
    border: 10px solid var(--green); box-sizing: border-box; background: var(--white);
    display: flex; align-items: center; justify-content: center; font-size: 22px; font-weight: 800; color: var(--brown);
  }
  .footer { left: 0; top: 905px; width: 849px; height: 295px; background: var(--green); color: var(--white); }
  .footer-mark { position: absolute; left: 57px; top: 25px; width: 140px; height: 140px; background: var(--white); display: flex; align-items: center; justify-content: center; }
  .footer-mark span { width: 84px; height: 84px; border-radius: 50%; background: var(--green); }
  .footer-name { position: absolute; left: 226px; top: 22px; font-size: 44px; font-weight: 800; }
  .footer-en { position: absolute; left: 228px; top: 80px; font-size: 20px; font-weight: 700; }
  .footer-tel { position: absolute; left: 226px; top: 105px; font-size: 58px; font-weight: 800; display: flex; align-items: center; gap: 10px; }
  .footer-address { position: absolute; left: 57px; top: 185px; font-size: 14px; }
  .footer-mark-name { position: absolute; left: 57px; top: 170px; font-size: 12px; font-weight: 700; }
  .footer-url { position: absolute; left: 0; right: 0; bottom: 34px; text-align: center; font-size: 26px; font-weight: 700; }
</style>
</head>
<body>
<div class="flyer">
  <div class="abs tagline">地域のホームドクターを目指して</div>
  <h1 class="abs clinic-title" style="margin:0">はるかぜ<span class="accent">ペット</span>クリニック</h1>
  <div class="abs open-date">3月24日<small>(月)</small></div>
  <div class="abs open-word"><div class="open-ring">開院</div>PEN</div>

  <div class="abs puppy-photo" role="img" aria-label="こちらを見つめる子犬の写真"></div>

  <div class="abs preview-badge">
    <div class="lead">ご挨拶もかねて</div>
    <div class="event">内覧会開催</div>
    <div class="dates">3月21日(金)22日(土)</div>
    <div class="invite">皆様お気軽に遊びに<br>いらしてください</div>
  </div>

  <section class="abs greeting">
    <div class="greeting-head">
      <div class="greeting-icon" role="img" aria-label="院長のイラスト"></div>
      <h2>院長からのご挨拶</h2>
    </div>
    <p>はじめまして、はるかぜペットクリニック院長の森岡健司です。大学卒業後、熊本市内の動物病院で7年間勤務し、2014年3月24日に動物病院を開院することになりました。ホームドクターとして地域の皆様に親しまれる病院であるとともに、飼い主様と一緒に家族である動物たちの最善のケアができるように努めてまいりたいと思います。ワンちゃん達が遊べるスペースも少しですが用意してあります。ぜひ気軽に遊びにいらしてください。今後ともよろしくお願い致します。</p>
  </section>

  <div class="abs animals"><span class="label">対象動物</span>犬・猫・ウサギ・ハムスターなど</div>

  <table class="abs hours">
    <tr><th class="label-cell">診察時間</th><th>月</th><th>火</th><th>水</th><th>木</th><th>金</th><th>土</th><th>日・祝</th></tr>
    <tr><td class="time">9:00〜12:00</td><td class="dot">●</td><td class="dot">●</td><td class="dot">●</td><td class="dot">●</td><td class="dot">●</td><td class="dot">●</td><td class="closed">休診</td></tr>
    <tr><td class="time">15:30〜19:30</td><td class="dot">●</td><td class="dot">●</td><td class="dot">●</td><td class="dot">●</td><td class="dot">●</td><td class="closed">18:00<br>まで</td><td class="closed">休診</td></tr>
  </table>
  <div class="abs note">※予約優先となります</div>

  <div class="abs map" role="img" aria-label="病院周辺の地図">MAP</div>

  <footer class="abs footer">
    <div class="footer-mark"><span></span></div>
    <div class="footer-mark-name">はるかぜペットクリニック</div>
    <div class="footer-name">はるかぜペットクリニック</div>
    <div class="footer-en">Harukaze Pet Clinic</div>
    <div class="footer-tel">
      <svg width="46" height="46" viewBox="0 0 24 24" aria-hidden="true"><path fill="#fff" d="M6.6 10.8a15.1 15.1 0 0 0 6.6 6.6l2.2-2.2a1 1 0 0 1 1-.25 11.4 11.4 0 0 0 3.6.57 1 1 0 0 1 1 1V20a1 1 0 0 1-1 1A17 17 0 0 1 3 4a1 1 0 0 1 1-1h3.5a1 1 0 0 1 1 1c0 1.25.2 2.45.57 3.57a1 1 0 0 1-.25 1z"/></svg>
      096-555-0142
    </div>
    <div class="footer-address">住所：熊本市東区花立1丁目2-3　FAX：096-555-0143</div>
    <div class="footer-url">http://harukaze-petclinic.example</div>
  </footer>
</div>
</body>
</html>
```